Breezeway Travel NI needs a new Website

We have an old website that is just that - old. We need a fresh website that is professional graphic designed that has the following features.
1. Can be updated by ourselves in some areas.
2. Has a shopping cart.
3. Has links to download PDF files
4. Has links to other pages in the website
5. Includes social media links
6. Has a client log-in area
Full details in brief provided.

SORRY BUT IT'S URGENT. We've taken too long to write the details and it is now urgent. So my apologies I will be asking for designers to work quickly.

We will continue to use our existing web hosting company and url. Their is a link to the old website in the Design Brief.
Updates

UPDATE:  Please see the new file UPDATE TO DESIGN BRIEF.
Thanks for all your submissions to date.  We hope the update will assist with your designs.
As indicated in previous messages, we are happy with the Home Page + 1 Page in order to select the designer to work with in creating the full design. 

Thankyou Designers.  Much appreciate your efforts.
It's getting late here on Norfolk so I won't have much chance too review any more designs this evening.
But for your information:
Designer 3817405 Ravindra Sethi is so far the closest to what we are seeking.
Thanks again. 

Reason: Have extended to Monday 7 October to give time for designers to submit after feedback today. Especially given the time differences

Target Market(s)

Very wide audience. Current client group not that tech savvy, but we hope to broaden our market and sell more creative products, and so website needs to consider how people now use media, ie tablets & iphones.

Industry/Entity Type

Shopping

Requirements
Nice to have
• PLEASE SEE THE "UPDATE TO THE DESIGN BRIEF"

```html
<!DOCTYPE html>
<html lang="en">
<head>
<meta charset="utf-8">
<title>Breezeway Travel NI – Home</title>
<link rel="stylesheet" href="https://fonts.googleapis.com/css2?family=Questrial&family=Oswald:wght@500;600&display=swap">
<style>
  :root {
    --sky-top: #1a2f86;
    --sky-mid: #2d63b4;
    --sky-low: #5f9fd4;
    --sea: #35c2cf;
    --sea-light: #8fded8;
    --sand: #e6ded0;
    --sand-dark: #d6cab6;
    --orange: #f28a22;
    --ink: #141414;
    --text-grey: #5a5a5a;
    --white: #ffffff;
    --footer: #000000;
    --footer-grey: #9a9a9a;
    --social-blue: #2a58a8;
  }
  * { margin: 0; padding: 0; box-sizing: border-box; }
  html, body { width: 1200px; height: 800px; overflow: hidden; }
  body { font-family: "Questrial", sans-serif; color: var(--ink); position: relative; background: var(--footer); }

  .hero-scene {
    position: absolute; left: 0; top: 0; width: 1200px; height: 729px;
    background: linear-gradient(180deg,
      var(--sky-top) 0px, var(--sky-mid) 170px, var(--sky-low) 310px,
      var(--sea) 325px, var(--sea-light) 370px,
      var(--sand) 400px, var(--sand-dark) 560px, var(--sand) 729px);
  }
  .abs { position: absolute; }

  .cart { left: 815px; top: 16px; color: var(--white); font-size: 13px; display: flex; align-items: center; gap: 6px; }
  .divider { left: 930px; top: 18px; width: 1px; height: 14px; border-left: 1px dotted rgba(255,255,255,.6); }
  .social-dot { width: 24px; height: 24px; border-radius: 50%; background: var(--social-blue); border: 2px solid rgba(255,255,255,.8); }

  .brand { left: 470px; top: 26px; display: flex; align-items: center; gap: 12px; }
  .brand-mark { width: 80px; height: 80px; border-radius: 50%; background: var(--orange); }
  .brand-name { font-family: "Questrial", sans-serif; color: var(--orange); font-size: 28px; line-height: 1; width: 170px; }

  .main-nav { left: 289px; top: 115px; display: flex; align-items: center; gap: 0; }
  .nav-item { color: var(--white); font-size: 14px; padding: 2px 10px; margin-right: 4px; display: flex; align-items: center; gap: 3px; }
  .nav-item.active { background: var(--orange); padding: 2px 11px; }
  .caret { width: 0; height: 0; border-left: 4px solid transparent; border-right: 4px solid transparent; border-top: 4px solid var(--white); }

  .headline { left: 375px; top: 180px; font-family: "Oswald", sans-serif; font-weight: 600; font-size: 34px; letter-spacing: -.5px; }
  .established { left: 377px; top: 223px; font-size: 14px; }
  .promotes { left: 376px; top: 249px; color: var(--orange); font-size: 20px; letter-spacing: .5px; }
  .values { left: 376px; top: 276px; font-size: 14px; word-spacing: 8px; letter-spacing: .3px; }
  .supported { left: 377px; top: 299px; color: var(--white); font-size: 22px; font-weight: bold; letter-spacing: .5px; }

  .services { left: 360px; top: 330px; display: flex; }
  .service { width: 78px; text-align: center; font-family: "Oswald", sans-serif; font-weight: 500; font-size: 12px; }
  .service svg { display: block; margin: 0 auto 6px; height: 34px; }

  .contact-panel { left: 797px; top: 332px; width: 204px; height: 385px; background: rgba(255,255,255,.9); border-radius: 3px; padding: 12px 14px 0 37px; }
  .contact-block { position: relative; padding-bottom: 10px; margin-bottom: 14px; border-bottom: 1px dashed #333; }
  .contact-block:last-child { border-bottom: none; }
  .contact-block svg { position: absolute; left: -25px; top: 1px; }
  .contact-title { font-size: 12px; color: #222; margin-bottom: 6px; letter-spacing: .2px; }
  .contact-text { font-size: 9.5px; color: var(--text-grey); line-height: 1.3; letter-spacing: .3px; }

  .tagline { left: 199px; top: 643px; font-size: 19px; letter-spacing: -.3px; }
  .needs { font-size: 11px; color: #222; list-style: none; }
  .needs li { position: absolute; padding-left: 18px; }
  .needs li::before { content: ""; position: absolute; left: 0; top: 4px; width: 6px; height: 6px; border-radius: 50%; background: var(--ink); }

  .site-footer { position: absolute; left: 0; top: 729px; width: 1200px; height: 71px; background: var(--footer); }
  .copyright { position: absolute; left: 0; width: 1097px; top: 48px; text-align: center; color: #cfcfcf; font-size: 11px; }
  .footer-brand { position: absolute; left: 860px; top: 14px; display: flex; align-items: center; gap: 10px; }
  .footer-brand .mark { width: 46px; height: 46px; border-radius: 50%; background: var(--footer-grey); }
  .footer-brand .name { color: var(--footer-grey); font-size: 16px; line-height: 1; width: 80px; }
</style>
</head>
<body>
  <div class="hero-scene" role="img" aria-label="Beach photograph: deep blue sky, turquoise sea with rocky headland and a kangaroo resting on white sand"></div>

  <header>
    <div class="abs cart">
      <svg width="20" height="18" viewBox="0 0 20 18" fill="none" stroke="#fff" stroke-width="1.5"><path d="M1 2h3l3 10h10l2-7H5"/><circle cx="8" cy="15.5" r="1.3"/><circle cx="15" cy="15.5" r="1.3"/></svg>
      shopping cart
    </div>
    <div class="abs divider"></div>
    <a class="abs social-dot" style="left:943px;top:13px" aria-label="Social page link"></a>
    <a class="abs social-dot" style="left:972px;top:13px" aria-label="Social feed link"></a>

    <div class="abs brand">
      <div class="brand-mark"></div>
      <div class="brand-name">Breezeway Travel NI</div>
    </div>

    <nav class="abs main-nav">
      <span class="nav-item active">Home</span>
      <span class="nav-item">Overview <i class="caret"></i></span>
      <span class="nav-item">Norfolk Island Services <i class="caret"></i></span>
      <span class="nav-item">Our Shop <i class="caret"></i></span>
      <span class="nav-item">Make a Booking <i class="caret"></i></span>
      <span class="nav-item">Testimonials <i class="caret"></i></span>
    </nav>
  </header>

  <main>
    <h1 class="abs headline">OUR SOCIAL ENTERPRISE</h1>
    <p class="abs established">Established July 2001</p>
    <p class="abs promotes">PROMOTES</p>
    <p class="abs values">DIVERSITY CARING COMMUNITY NORFOLK ISLAND</p>
    <p class="abs supported">SUPPORTED</p>

    <div class="abs services">
      <div class="service">
        <svg width="42" height="34" role="img" aria-label="Surfer icon"><rect x="4" y="4" width="34" height="26" rx="13" fill="var(--orange)"/></svg>HOLIDAYS
      </div>
      <div class="service">
        <svg width="40" height="34" viewBox="0 0 40 34"><rect x="14" y="2" width="12" height="7" rx="2" fill="none" stroke="var(--orange)" stroke-width="3"/><rect x="3" y="8" width="34" height="24" rx="3" fill="var(--orange)"/></svg>TRAVEL
      </div>
      <div class="service">
        <svg width="50" height="34" role="img" aria-label="Recreation icon"><rect x="2" y="8" width="46" height="18" rx="9" fill="var(--orange)"/></svg>RECREATION
      </div>
      <div class="service">
        <svg width="34" height="34" viewBox="0 0 34 34"><circle cx="17" cy="17" r="12" fill="none" stroke="var(--orange)" stroke-width="7"/><circle cx="17" cy="17" r="12" fill="none" stroke="#fff" stroke-width="7" stroke-dasharray="5 13.85"/></svg>RESPITE
      </div>
      <div class="service">
        <svg width="40" height="34" viewBox="0 0 40 34"><rect x="2" y="6" width="36" height="24" rx="2" fill="var(--orange)"/></svg>PROJECTS
      </div>
    </div>

    <aside class="abs contact-panel">
      <div class="contact-block">
        <svg width="14" height="12" viewBox="0 0 14 12"><path d="M1 2l4-1 4 1 4-1v9l-4 1-4-1-4 1z" fill="#8a8a8a"/></svg>
        <h2 class="contact-title">LOCATION &amp; CONTACTS</h2>
        <p class="contact-text">Cascade Lane, Burnt Pine<br>PO Box 514<br>Norfolk Island NSW 2899<br>SOUTH PACIFIC<br>N.B.N. 417 062 358</p>
      </div>
      <div class="contact-block">
        <svg width="14" height="12" viewBox="0 0 14 12"><path d="M1 5c0-3 12-3 12 0v1H10V4H4v2H1z M3 7h8l1 4H2z" fill="#8a8a8a"/></svg>
        <h2 class="contact-title">TELEPHONE</h2>
        <p class="contact-text">International + 67 23 51907<br>Australia 1800 463 218<br>New Zealand</p>
      </div>
      <div class="contact-block">
        <svg width="14" height="12" viewBox="0 0 14 12"><rect x="1" y="2" width="12" height="8" fill="#8a8a8a"/><path d="M1 2l6 5 6-5" fill="none" stroke="#fff"/></svg>
        <h2 class="contact-title">EMAIL WEBSITE &amp; SOCIAL</h2>
        <p class="contact-text">hello@breezewaytravel.org<br>www.breezewaytravel.org<br>www.socialpage.net/<br>breezewaytravel</p>
      </div>
      <div class="contact-block">
        <svg width="14" height="12" viewBox="0 0 14 12"><rect x="1" y="2" width="12" height="9" fill="none" stroke="#8a8a8a" stroke-width="1.5"/><rect x="3" y="4" width="8" height="5" fill="#8a8a8a"/></svg>
        <h2 class="contact-title">IMAGES &amp; VIDEO</h2>
        <p class="contact-text">BREEZY HOLS VIDEO<br>to see more photographs and video's<br>LIKE our SOCIAL page</p>
      </div>
    </aside>

    <p class="abs tagline">For people requiring support to participate in socially inclusive events</p>
    <ul class="needs">
      <li style="left:200px;top:674px">Intellectual Disability</li>
      <li style="left:350px;top:674px">Acquired Brain Injury</li>
      <li style="left:483px;top:674px">Mental Health</li>
      <li style="left:610px;top:674px">Sensory Impairment</li>
      <li style="left:200px;top:701px">Frail Aged</li>
      <li style="left:350px;top:702px">Mobility Challenged</li>
      <li style="left:483px;top:702px">Siblings of children with Disabilities</li>
    </ul>
  </main>

  <footer class="site-footer">
    <a class="abs social-dot" style="left:530px;top:7px" aria-label="Social page link"></a>
    <a class="abs social-dot" style="left:558px;top:7px" aria-label="Social feed link"></a>
    <p class="copyright">© 2013 breezewaytravel.org. All rights reserved.</p>
    <div class="footer-brand">
      <div class="mark"></div>
      <div class="name">Breezeway Travel NI</div>
    </div>
  </footer>
</body>
</html>
```